Powerpoint template for Meadowlark Crossing

I need a powerpoint template for my business that would also work for Google slides.
I intermittently deliver training to people and I want a nice powerpoint template, that could also work in google docs to help make production easier and more seamless for me. I also sometimes product reports and analyses that are best done in powerpoint or Google slides. I need a title page, Title and content page, section heading page and any other pages that someone normally has!

Target Market(s)

Leaders and managers in medium to large companies. I provide training and coaching services to senior staff who have got 'stuck' and want help to find their way forward.

Font styles to use
Sans Serif

Requirements
Must have
• Colours and fonts to fit with logo please.
• Must include the logo and company name.
Nice to have
• a picture for the front?

```html
<!DOCTYPE html>
<html lang="en">
<head>
<meta charset="utf-8">
<title>Meadowlark Crossing – Presentation Template</title>
<link href="https://fonts.googleapis.com/css2?family=Open+Sans:wght@400;600;700&display=swap" rel="stylesheet">
<style>
:root{
  --teal:#17b095;
  --teal-dark:#148f86;
  --blue:#1f7fa3;
  --purple:#4b2e8f;
  --ink:#1c1c1c;
  --body:#3a3a3a;
  --grey:#d9d9d9;
  --grey-light:#efefef;
  --canvas:#e8e8e8;
  --red:#e8312f;
  --cream:#efe9d9;
}
*{box-sizing:border-box;margin:0;padding:0}
html,body{width:1200px;height:2651px;overflow:hidden;background:var(--canvas);font-family:"Open Sans",Arial,sans-serif;color:var(--body)}
.board{position:relative;width:1200px;height:2651px}
.slide{position:absolute;background:#fff;overflow:hidden;box-shadow:0 1px 3px rgba(0,0,0,.18)}
.photo{position:absolute;inset:0}
.photo-seedlings{background:radial-gradient(ellipse at 70% 20%,#d8e6a8 0%,#7fa04a 30%,#3e5a26 60%,#2a2a1c 100%)}
.photo-soil{background:linear-gradient(180deg,#6c8f3c 0%,#4a6a2a 55%,#5a4532 78%,#3b2b1e 100%)}
.photo-desk{background:linear-gradient(135deg,#4a5358,#2d3539 60%,#6a6a5c)}
.art{position:absolute;border-radius:6px}
.art-growth{background:linear-gradient(160deg,#e7f5ee,#fde9b0 70%,#f4d27a)}
.art-meeting{background:radial-gradient(circle at 50% 60%,#e9e6f3,#f6f6f8 70%)}
.h{font-weight:700;color:var(--ink);font-size:21px;line-height:1.2}
.h .accent{color:var(--teal)}
.center{text-align:center}
.p{font-size:7px;line-height:1.45;color:var(--body)}
.abs{position:absolute}
.footer-line{position:absolute;left:40px;right:40px;bottom:8px;height:1px;background:var(--teal)}
.footer-mark{position:absolute;right:8px;bottom:3px;width:16px;height:12px;background:var(--teal);clip-path:polygon(50% 0,100% 40%,100% 100%,0 100%,0 40%)}
.footer-name{position:absolute;left:8px;bottom:5px;font-size:5px;font-weight:600;color:var(--purple);display:flex;align-items:center;gap:3px}
.footer-name::before{content:"";width:7px;height:7px;border-radius:50%;background:var(--teal)}
.title-panel{position:absolute;top:0;background:rgba(255,255,255,.55);display:flex;flex-direction:column;align-items:center;justify-content:center;gap:12px;text-align:center}
.brand-dot{width:46px;height:46px;border-radius:50%;background:var(--teal)}
.brand-name{font-size:26px;font-weight:400;color:var(--purple);line-height:1.1;text-transform:uppercase}
.report-bar{position:absolute;background:rgba(215,215,215,.8);color:var(--purple);font-size:17px;display:flex;align-items:center;justify-content:center;letter-spacing:.5px}
.card{position:absolute;background:var(--grey);padding:34px 10px 8px}
.card .icon{position:absolute;top:-16px;left:50%;margin-left:-18px;width:36px;height:36px;border-radius:50%;background:#fff;border:3px solid var(--grey);display:flex;align-items:center;justify-content:center}
.label{position:absolute;color:#fff;font-size:8px;font-weight:700;display:flex;align-items:center;justify-content:center}
.num{position:absolute;width:30px;height:30px;border-radius:50%;color:#fff;font-weight:700;font-size:14px;display:flex;align-items:center;justify-content:center;border:3px solid #fff;box-shadow:0 0 0 1px #ccc}
.item-num{position:absolute;font-size:15px;color:var(--ink)}
.item-text{position:absolute;width:80px;font-size:6.5px;line-height:1.4}
.item-text b{display:block;font-size:6.5px;color:var(--ink)}
.band{position:absolute;left:0;right:0;bottom:0;height:66px;background:var(--ink);color:#fff;font-weight:700;font-size:12px;text-align:center;display:flex;align-items:center;justify-content:center;line-height:1.45}
.row-label{position:absolute;left:18px;width:110px;height:22px;color:#fff;font-size:6px;font-weight:700;display:flex;align-items:center;padding-left:6px}
.row-bg{position:absolute;left:18px;right:18px;height:22px;background:var(--grey-light)}
.stat{position:absolute;top:146px;width:49px;height:38px;background:var(--teal);color:#fff;font-size:6px;font-weight:700;display:flex;flex-direction:column;align-items:center;justify-content:center;gap:6px}
.sub{font-size:8px;font-weight:700;color:var(--ink)}
.points-head{position:absolute;height:12px;color:#fff;font-size:5.5px;font-weight:700;display:flex;align-items:center;justify-content:center}
.points-box{position:absolute;top:102px;height:168px}
.point{position:absolute;left:10px;right:8px;display:flex;gap:6px;align-items:flex-start}
.point b{display:block;font-size:5.5px}
.point span{font-size:5px;color:#8a8a8a}
.bar{position:absolute;bottom:28px;width:22px;height:118px;border-radius:11px;background:var(--grey);overflow:hidden}
.bar i{position:absolute;left:0;right:0;bottom:0;border-radius:11px}
.bar em{position:absolute;left:0;right:0;bottom:2px;height:18px;border-radius:50%;background:inherit;color:#fff;font-style:normal;font-size:7px;font-weight:700;display:flex;align-items:center;justify-content:center}
.contact-line{display:flex;flex-direction:column;gap:4px;color:#fff;font-size:7px;font-weight:700}
.contact-title{position:absolute;color:#fff;font-size:26px;font-weight:600}
</style>
</head>
<body>
<main class="board">

<!-- Row 1: cover slides -->
<section class="slide" style="left:21px;top:14px;width:562px;height:318px">
  <div class="photo photo-seedlings" role="img" aria-label="Photo of young seedlings sprouting from soil"></div>
  <div class="title-panel" style="left:166px;width:250px;height:222px">
    <div class="brand-dot"></div>
    <div class="brand-name">Meadowlark<br>Crossing</div>
  </div>
  <div class="report-bar" style="left:164px;top:272px;width:250px;height:38px">TITLE OF THE REPORT</div>
</section>

<section class="slide" style="left:615px;top:20px;width:558px;height:312px">
  <div class="photo photo-seedlings" role="img" aria-label="Photo of seedlings growing in sunlight"></div>
  <div class="title-panel" style="left:148px;width:242px;height:218px">
    <div class="brand-dot"></div>
    <div class="brand-name">Meadowlark<br>Crossing</div>
  </div>
  <div class="report-bar" style="left:148px;top:258px;width:248px;height:38px">TITLE OF THE REPORT</div>
</section>

<!-- Row 2 -->
<section class="slide" style="left:21px;top:346px;width:562px;height:317px">
  <h2 class="h abs" style="left:73px;top:52px">About <span class="accent">Company</span></h2>
  <div class="abs" style="left:32px;top:116px;width:240px">
    <p class="p">Lorem ipsum dolor sit amet, consectetur adipiscing elit, sed do eiusmod tempor incididunt ut labore et dolore magna aliqua. Ut enim ad minim veniam, quis nostrud exercitation ullamco laboris nisi ut aliquip ex ea commodo consequat. Lorem ipsum dolor sit amet, consectetur adipiscing elit, sed do eiusmod tempor incididunt ut labore et dolore magna aliqua.</p>
    <p class="p" style="margin-top:14px">Lorem ipsum dolor sit amet, consectetur adipiscing elit, sed do eiusmod tempor incididunt ut labore et dolore magna aliqua. Ut enim ad minim veniam, quis nostrud exercitation ullamco laboris nisi ut aliquip ex ea commodo consequat.</p>
    <p class="p" style="margin-top:14px">Aliquip ex ea commodo consequat. Lorem ipsum dolor sit amet, consectetur adipiscing elit, sed do eiusmod tempor incididunt ut labore et dolore magna aliqua.</p>
  </div>
  <div class="abs" style="left:340px;top:60px;width:200px;display:flex;flex-direction:column;align-items:center;gap:14px">
    <div class="brand-dot" style="width:70px;height:70px"></div>
    <div class="brand-name" style="font-size:27px;text-align:center">Meadowlark<br>Crossing</div>
  </div>
  <div class="footer-name">Meadowlark Crossing</div><div class="footer-line"></div><div class="footer-mark"></div>
</section>

<section class="slide" style="left:615px;top:346px;width:558px;height:317px">
  <h2 class="h abs" style="left:26px;top:135px;font-size:19px">Lorem ipsum <span class="accent">dolor</span></h2>
  <div class="abs" style="left:238px;top:48px;width:140px">
    <p class="p">Lorem ipsum dolor sit amet, consectetur adipiscing elit, sed do eiusmod tempor incididunt ut labore et dolore magna aliqua. Ut enim ad minim veniam, quis nostrud exercitation ullamco laboris nisi ut aliquip ex ea commodo consequat. Lorem ipsum dolor sit amet, consectetur adipiscing elit, sed do eiusmod tempor.</p>
    <p class="p" style="margin-top:14px">Lorem ipsum dolor sit amet, consectetur adipiscing elit, sed do eiusmod tempor incididunt ut labore et dolore magna aliqua. Ut enim ad minim veniam, quis nostrud exercitation ullamco laboris nisi ut aliquip ex ea commodo consequat.</p>
  </div>
  <div class="abs" style="left:396px;top:48px;width:140px">
    <p class="p">Lorem ipsum dolor sit amet, consectetur adipiscing elit, sed do eiusmod tempor incididunt ut labore et dolore magna aliqua. Ut enim ad minim veniam, quis nostrud exercitation ullamco.</p>
    <p class="p" style="margin-top:14px">Lorem ipsum dolor sit amet, consectetur adipiscing elit, sed do eiusmod tempor incididunt ut labore et dolore magna aliqua. Ut enim ad minim veniam, quis nostrud exercitation ullamco laboris nisi ut aliquip ex ea commodo consequat.</p>
  </div>
  <div class="footer-name">Meadowlark Crossing</div><div class="footer-line"></div><div class="footer-mark"></div>
</section>

<!-- Row 3 -->
<section class="slide" style="left:21px;top:675px;width:562px;height:315px">
  <h2 class="h abs center" style="left:0;right:0;top:16px">Lorem ipsum <span class="accent">dolor</span></h2>
  <p class="p abs center" style="left:150px;right:150px;top:46px">Lorem ipsum dolor sit amet, consectetur adipiscing elit, sed do eiusmod tempor incididunt ut labore et dolore magna aliqua.</p>
  <div class="card" style="left:62px;top:128px;width:125px;height:130px">
    <div class="icon"><svg width="18" height="18" viewBox="0 0 18 18"><circle cx="9" cy="9" r="6" fill="none" stroke="var(--teal)" stroke-width="3" stroke-dasharray="3 1.7"/><circle cx="9" cy="9" r="2.5" fill="var(--teal)"/></svg></div>
    <p class="p">Lorem ipsum dolor sit amet, consectetur adipiscing elit, sed do eiusmod tempor incididunt ut labore et dolore magna aliqua. sed do eiusmod tempor incididunt ut labore et dolore magna aliqua.</p>
  </div>
  <div class="card" style="left:218px;top:128px;width:125px;height:130px">
    <div class="icon"><svg width="18" height="18" viewBox="0 0 18 18"><circle cx="9" cy="9" r="7" fill="none" stroke="var(--teal)" stroke-width="1.5"/><circle cx="9" cy="9" r="4" fill="none" stroke="var(--teal)" stroke-width="1.5"/><circle cx="9" cy="9" r="1.5" fill="var(--teal)"/></svg></div>
    <p class="p">Lorem ipsum dolor sit amet, consectetur adipiscing elit, sed do eiusmod tempor incididunt ut labore et dolore magna aliqua. sed do eiusmod tempor incididunt ut labore et dolore magna aliqua.</p>
  </div>
  <div class="card" style="left:374px;top:128px;width:125px;height:130px">
    <div class="icon"><svg width="18" height="18" viewBox="0 0 18 18"><g fill="var(--teal)"><rect x="2" y="10" width="3" height="6"/><rect x="7" y="7" width="3" height="9"/><rect x="12" y="3" width="3" height="13"/></g></svg></div>
    <p class="p">Lorem ipsum dolor sit amet, consectetur adipiscing elit, sed do eiusmod tempor incididunt ut labore et dolore magna aliqua. sed do eiusmod tempor incididunt ut labore et dolore magna aliqua.</p>
  </div>
  <div class="footer-name">Meadowlark Crossing</div><div class="footer-line"></div><div class="footer-mark"></div>
</section>

<section class="slide" style="left:615px;top:675px;width:558px;height:315px">
  <h2 class="h abs center" style="left:0;right:0;top:16px">Lorem ipsum <span class="accent">dolor</span></h2>
  <p class="p abs center" style="left:120px;right:120px;top:46px">Lorem ipsum dolor sit amet, consectetur adipiscing elit, sed do eiusmod tempor incididunt ut labore et dolore magna aliqua. Lorem ipsum dolor sit amet, consectetur adipiscing elit, sed do eiusmod tempor incididunt ut labore et dolore magna aliqua.</p>
  <div class="abs" style="left:24px;top:120px;width:254px;height:160px;border:2px solid var(--teal);border-radius:12px"></div>
  <div class="label" style="left:68px;top:110px;width:146px;height:22px;background:var(--teal);border-radius:11px;font-size:9px">Lorem ipsum dolor</div>
  <p class="p abs" style="left:36px;top:144px;width:230px">Lorem ipsum dolor sit amet, consectetur adipiscing elit, sed do eiusmod tempor incididunt ut labore et dolore magna aliqua. Lorem ipsum dolor sit amet, consectetur adipiscing elit, sed do eiusmod tempor incididunt ut labore et dolore magna aliqua.</p>
  <svg class="abs" style="left:44px;top:212px" width="210" height="48" viewBox="0 0 210 48" font-family="Open Sans, sans-serif" font-size="5">
    <rect x="0" y="0" width="210" height="10" fill="#fff"/>
    <rect x="50" y="0" width="160" height="10" fill="var(--teal)"/>
    <g fill="#fff" text-anchor="middle"><text x="70" y="7">Text</text><text x="110" y="7">Text</text><text x="150" y="7">Text</text><text x="190" y="7">Text</text></g>
    <rect x="0" y="12" width="210" height="10" fill="#f0f0f0"/>
    <rect x="0" y="24" width="210" height="10" fill="#fff"/>
    <g fill="#555" text-anchor="middle"><text x="22" y="19">Add Text</text><text x="70" y="19">Text</text><text x="110" y="19">Text</text><text x="150" y="19">Text</text><text x="190" y="19">Text</text>
    <text x="22" y="31">Add Text</text><text x="70" y="31">Text</text><text x="110" y="31">Text</text><text x="150" y="31">Text</text><text x="190" y="31">Text</text></g>
  </svg>
  <div class="art art-growth" style="left:298px;top:84px;width:240px;height:190px" role="img" aria-label="Illustration of a watering can over plants growing from stacks of coins"></div>
  <div class="footer-name">Meadowlark Crossing</div><div class="footer-line"></div><div class="footer-mark"></div>
</section>

<!-- Row 4 -->
<section class="slide" style="left:21px;top:1004px;width:562px;height:314px">
  <div class="label" style="left:30px;top:132px;width:118px;height:28px;background:var(--teal)">Lorem ipsum dolor</div>
  <div class="label" style="left:166px;top:132px;width:118px;height:28px;background:var(--blue)">Lorem ipsum dolor</div>
  <div class="label" style="left:302px;top:132px;width:118px;height:28px;background:var(--purple)">Lorem ipsum dolor</div>
  <div class="label" style="left:438px;top:132px;width:118px;height:28px;background:var(--teal)">Lorem ipsum dolor</div>
  <div class="num" style="left:34px;top:88px;background:var(--teal)">1</div>
  <div class="num" style="left:170px;top:172px;background:var(--blue)">2</div>
  <div class="num" style="left:306px;top:88px;background:var(--purple)">3</div>
  <div class="num" style="left:442px;top:172px;background:var(--teal)">4</div>
  <p class="p abs" style="left:34px;top:176px;width:90px">Lorem ipsum dolor sit amet, consectetur adipiscing elit, sed do eiusmod tempor incididunt ut labore et dolore magna aliqua.</p>
  <p class="p abs" style="left:192px;top:56px;width:90px">Lorem ipsum dolor sit amet, consectetur adipiscing elit, sed do eiusmod tempor incididunt ut labore et dolore magna aliqua.</p>
  <p class="p abs" style="left:318px;top:176px;width:90px">Lorem ipsum dolor sit amet, consectetur adipiscing elit, sed do eiusmod tempor incididunt ut labore et dolore magna aliqua.</p>
  <p class="p abs" style="left:462px;top:50px;width:90px">Lorem ipsum dolor sit amet, consectetur adipiscing elit, sed do eiusmod tempor incididunt ut labore et dolore magna aliqua.</p>
  <div class="footer-name">Meadowlark Crossing</div><div class="footer-line"></div><div class="footer-mark"></div>
</section>

<section class="slide" style="left:615px;top:1004px;width:558px;height:314px">
  <h2 class="h abs center" style="left:0;right:0;top:22px">Lorem ipsum <span class="accent">dolor</span></h2>
  <div class="item-num" style="left:84px;top:76px">01</div>
  <div class="item-num" style="left:214px;top:76px">02</div>
  <div class="item-num" style="left:356px;top:76px">03</div>
  <div class="item-num" style="left:84px;top:158px">05</div>
  <div class="item-num" style="left:214px;top:158px">06</div>
  <div class="item-num" style="left:356px;top:158px">07</div>
  <p class="p item-text" style="left:120px;top:78px"><b>Lorem ipsum dolor</b>Lorem ipsum dolor sit amet, consectetur adipiscing elit, sed do eiusmod tempor incididunt ut labore.</p>
  <p class="p item-text" style="left:250px;top:78px"><b>Lorem ipsum dolor</b>Lorem ipsum dolor sit amet, consectetur adipiscing elit, sed do eiusmod tempor incididunt ut labore.</p>
  <p class="p item-text" style="left:392px;top:78px"><b>Lorem ipsum dolor</b>Lorem ipsum dolor sit amet, consectetur adipiscing elit, sed do eiusmod tempor incididunt ut labore.</p>
  <p class="p item-text" style="left:120px;top:160px"><b>Lorem ipsum dolor</b>Lorem ipsum dolor sit amet, consectetur adipiscing elit, sed do eiusmod tempor incididunt ut labore.</p>
  <p class="p item-text" style="left:250px;top:160px"><b>Lorem ipsum dolor</b>Lorem ipsum dolor sit amet, consectetur adipiscing elit, sed do eiusmod tempor incididunt ut labore.</p>
  <p class="p item-text" style="left:392px;top:160px"><b>Lorem ipsum dolor</b>Lorem ipsum dolor sit amet, consectetur adipiscing elit, sed do eiusmod tempor incididunt ut labore.</p>
  <div class="band">Lorem ipsum dolor sit amet, consectetur adipiscing elit,<br>sed do eiusmod tempor</div>
</section>

<!-- Row 5 -->
<section class="slide" style="left:0;top:1334px;width:408px;height:230px">
  <h2 class="h abs center" style="left:0;right:0;top:22px;font-size:18px">Lorem ipsum <span class="accent">dolor</span></h2>
  <div class="row-bg" style="top:80px"></div><div class="row-bg" style="top:110px"></div><div class="row-bg" style="top:140px"></div>
  <div class="row-label" style="top:80px;width:100px;background:var(--teal-dark)">Lorem ipsum dolor</div>
  <div class="row-label" style="top:110px;width:100px;background:#2fb3b0">Lorem ipsum dolor</div>
  <div class="row-label" style="top:140px;width:100px;background:#7fcfd6">Lorem ipsum dolor</div>
  <p class="p abs" style="left:140px;top:83px;width:240px;font-size:5.5px">Lorem ipsum dolor sit amet, consectetur adipiscing elit, sed do eiusmod tempor incididunt ut labore et dolore magna aliqua.</p>
  <p class="p abs" style="left:140px;top:113px;width:240px;font-size:5.5px">Lorem ipsum dolor sit amet, consectetur adipiscing elit, sed do eiusmod tempor incididunt ut labore et dolore magna aliqua.</p>
  <p class="p abs" style="left:140px;top:143px;width:240px;font-size:5.5px">Lorem ipsum dolor sit amet, consectetur adipiscing elit, sed do eiusmod tempor incididunt ut labore et dolore magna aliqua.</p>
  <div class="footer-name">Meadowlark Crossing</div><div class="footer-line"></div><div class="footer-mark"></div>
</section>

<section class="slide" style="left:413px;top:1334px;width:392px;height:230px">
  <svg class="abs" style="left:100px;top:24px" width="200" height="108" viewBox="0 0 200 108">
    <g stroke="#fff" stroke-width="3">
      <path d="M10 100 A90 90 0 0 1 36.4 36.4 L71.7 71.7 A40 40 0 0 0 60 100 Z" fill="var(--teal)"/>
      <path d="M36.4 36.4 A90 90 0 0 1 100 10 L100 60 A40 40 0 0 0 71.7 71.7 Z" fill="var(--teal-dark)"/>
      <path d="M100 10 A90 90 0 0 1 163.6 36.4 L128.3 71.7 A40 40 0 0 0 100 60 Z" fill="var(--teal)"/>
      <path d="M163.6 36.4 A90 90 0 0 1 190 100 L140 100 A40 40 0 0 0 128.3 71.7 Z" fill="var(--teal-dark)"/>
    </g>
    <circle cx="100" cy="100" r="34" fill="var(--teal)" stroke="#fff" stroke-width="3"/>
    <g fill="none" stroke="#fff" stroke-width="2">
      <circle cx="100" cy="92" r="6"/><path d="M88 110 Q100 96 112 110"/>
      <circle cx="40" cy="72" r="6"/><circle cx="78" cy="34" r="6"/><circle cx="122" cy="34" r="6"/><path d="M154 78 L168 66 L158 82 Z"/>
    </g>
  </svg>
  <div class="abs" style="left:38px;top:8px;font-size:7px;font-weight:600;color:var(--ink)">1. Lorem ipsum dolor</div>
  <div class="abs" style="left:14px;top:84px;font-size:7px;font-weight:600;color:var(--ink)">2. Lorem ipsum dolor</div>
  <div class="abs" style="left:276px;top:8px;font-size:7px;font-weight:600;color:var(--ink)">3. Lorem ipsum dolor</div>
  <div class="abs" style="left:300px;top:84px;font-size:7px;font-weight:600;color:var(--ink)">4. Lorem ipsum dolor</div>
  <h2 class="h abs center" style="left:0;right:0;top:146px;font-size:19px">Lorem ipsum <span class="accent">dolor</span></h2>
  <div class="footer-name">Meadowlark Crossing</div><div class="footer-line"></div><div class="footer-mark"></div>
</section>

<section class="slide" style="left:809px;top:1334px;width:391px;height:230px">
  <div class="photo photo-desk" style="bottom:auto;height:132px" role="img" aria-label="Photo of a team working around a desk"></div>
  <h2 class="abs" style="left:0;right:0;top:40px;text-align:center;color:#fff;font-size:16px;font-weight:700">Lorem ipsum dolor</h2>
  <div class="stat" style="left:86px"><span>⚙</span>$18,000</div>
  <div class="stat" style="left:144px"><span>⌕</span>$45,000</div>
  <div class="stat" style="left:202px"><span>✉</span>$35,000</div>
  <div class="stat" style="left:260px"><span>▮</span>$46,000</div>
  <p class="p abs" style="left:24px;right:24px;top:196px;font-size:5px">Lorem ipsum dolor sit amet, consectetur adipiscing elit, sed do eiusmod tempor incididunt ut labore et dolore magna aliqua. Ut enim ad minim veniam, quis nostrud exercitation ullamco laboris nisi ut aliquip ex ea commodo.</p>
  <div class="footer-line"></div><div class="footer-mark"></div>
</section>

<!-- Row 6 -->
<section class="slide" style="left:21px;top:1576px;width:562px;height:315px">
  <div class="art art-meeting" style="left:22px;top:38px;width:240px;height:220px" role="img" aria-label="Illustration of three colleagues meeting around a table"></div>
  <h2 class="h abs" style="left:280px;top:20px;font-size:22px">Lorem ipsum <span class="accent">dolor</span></h2>
  <div class="abs" style="left:280px;top:66px;width:260px">
    <p class="sub">Lorem ipsum dolor</p>
    <p class="p" style="margin-top:4px">Lorem ipsum dolor sit amet, consectetur adipiscing elit, sed do eiusmod tempor incididunt ut labore et dolore magna aliqua. Lorem ipsum dolor sit amet, consectetur adipiscing elit, sed do eiusmod tempor incididunt</p>
    <p class="sub" style="margin-top:12px">Lorem ipsum dolor</p>
    <p class="p" style="margin-top:4px">Lorem ipsum dolor sit amet, consectetur adipiscing elit, sed do eiusmod tempor incididunt ut labore et dolore magna aliqua. Lorem ipsum dolor sit amet, consectetur adipiscing elit, sed do eiusmod tempor incididunt</p>
    <p class="sub" style="margin-top:12px">Lorem ipsum dolor</p>
    <p class="p" style="margin-top:4px">Lorem ipsum dolor sit amet, consectetur adipiscing elit, sed do eiusmod tempor incididunt ut labore et dolore magna aliqua. Lorem ipsum dolor sit amet, consectetur adipiscing elit, sed do eiusmod tempor incididunt</p>
  </div>
  <div class="footer-name">Meadowlark Crossing</div><div class="footer-line"></div><div class="footer-mark"></div>
</section>

<section class="slide" style="left:615px;top:1576px;width:558px;height:315px">
  <h2 class="h abs center" style="left:0;right:0;top:18px;font-size:22px">Lorem ipsum <span class="accent">dolor</span></h2>
  <svg class="abs" style="left:150px;top:54px" width="40" height="40" viewBox="0 0 40 40"><circle cx="20" cy="20" r="17" fill="none" stroke="var(--teal)" stroke-width="3"/><path d="M12 20 L18 26 L29 14" fill="none" stroke="var(--teal)" stroke-width="3"/></svg>
  <svg class="abs" style="left:360px;top:54px" width="40" height="40" viewBox="0 0 40 40"><circle cx="20" cy="20" r="17" fill="none" stroke="var(--red)" stroke-width="3"/><path d="M13 13 L27 27 M27 13 L13 27" stroke="var(--red)" stroke-width="3"/></svg>
  <div class="points-head" style="left:86px;top:102px;width:180px;background:var(--teal)">POSITIVE POINTS</div>
  <div class="points-head" style="left:286px;top:102px;width:180px;background:var(--red)">NEGATIVE POINTS</div>
  <div class="points-box" style="left:86px;top:114px;width:180px;height:156px;background:var(--cream)">
    <div class="point" style="top:12px"><svg width="12" height="12"><circle cx="6" cy="6" r="5" fill="none" stroke="var(--teal)"/><path d="M3.5 6 L5.5 8 L8.5 4" fill="none" stroke="var(--teal)"/></svg><div><b style="color:var(--teal)">TITLE GOES HERE</b><span>This is a sample text. Add your text here.</span></div></div>
    <div class="point" style="top:48px"><svg width="12" height="12"><circle cx="6" cy="6" r="5" fill="none" stroke="var(--teal)"/><path d="M3.5 6 L5.5 8 L8.5 4" fill="none" stroke="var(--teal)"/></svg><div><b style="color:var(--teal)">TITLE GOES HERE</b><span>This is a sample text. Add your text here.</span></div></div>
    <div class="point" style="top:84px"><svg width="12" height="12"><circle cx="6" cy="6" r="5" fill="none" stroke="var(--teal)"/><path d="M3.5 6 L5.5 8 L8.5 4" fill="none" stroke="var(--teal)"/></svg><div><b style="color:var(--teal)">TITLE GOES HERE</b><span>This is a sample text. Add your text here.</span></div></div>
    <div class="point" style="top:120px"><svg width="12" height="12"><circle cx="6" cy="6" r="5" fill="none" stroke="var(--teal)"/><path d="M3.5 6 L5.5 8 L8.5 4" fill="none" stroke="var(--teal)"/></svg><div><b style="color:var(--teal)">TITLE GOES HERE</b><span>This is a sample text. Add your text here.</span></div></div>
  </div>
  <div class="points-box" style="left:286px;top:114px;width:180px;height:156px;background:var(--grey-light)">
    <div class="point" style="top:12px"><svg width="12" height="12"><circle cx="6" cy="6" r="5" fill="none" stroke="var(--red)"/><path d="M4 4 L8 8 M8 4 L4 8" stroke="var(--red)"/></svg><div><b style="color:var(--red)">TITLE GOES HERE</b><span>This is a sample text. Add your text here.</span></div></div>
    <div class="point" style="top:48px"><svg width="12" height="12"><circle cx="6" cy="6" r="5" fill="none" stroke="var(--red)"/><path d="M4 4 L8 8 M8 4 L4 8" stroke="var(--red)"/></svg><div><b style="color:var(--red)">TITLE GOES HERE</b><span>This is a sample text. Add your text here.</span></div></div>
    <div class="point" style="top:84px"><svg width="12" height="12"><circle cx="6" cy="6" r="5" fill="none" stroke="var(--red)"/><path d="M4 4 L8 8 M8 4 L4 8" stroke="var(--red)"/></svg><div><b style="color:var(--red)">TITLE GOES HERE</b><span>This is a sample text. Add your text here.</span></div></div>
    <div class="point" style="top:120px"><svg width="12" height="12"><circle cx="6" cy="6" r="5" fill="none" stroke="var(--red)"/><path d="M4 4 L8 8 M8 4 L4 8" stroke="var(--red)"/></svg><div><b style="color:var(--red)">TITLE GOES HERE</b><span>This is a sample text. Add your text here.</span></div></div>
  </div>
  <div class="footer-name">Meadowlark Crossing</div><div class="footer-line"></div><div class="footer-mark"></div>
</section>

<!-- Row 7 -->
<section class="slide" style="left:21px;top:1905px;width:562px;height:314px">
  <h2 class="h abs center" style="left:0;right:0;top:30px;font-size:22px">Lorem ipsum <span class="accent">dolor</span></h2>
  <div class="abs" style="left:30px;top:108px;width:112px;height:112px;border-radius:50%;background:conic-gradient(var(--blue) 0 15%,var(--purple) 15% 35%,var(--teal) 35% 100%)"></div>
  <div class="abs" style="left:92px;top:120px;font-size:12px;font-weight:700;color:#fff">15</div>
  <div class="abs" style="left:42px;top:150px;font-size:12px;font-weight:700;color:#fff">20</div>
  <div class="abs" style="left:96px;top:178px;font-size:14px;font-weight:700;color:#fff">65</div>
  <div class="abs" style="left:200px;top:80px;width:120px">
    <p class="sub" style="font-size:7px">Lorem ipsum dolor</p>
    <p class="p" style="margin-top:3px">Lorem ipsum dolor sit amet, consectetur adipiscing elit, sed do eiusmod tempor incididunt ut labore et dolore magna aliqua.</p>
    <p class="sub" style="font-size:7px;margin-top:10px">Lorem ipsum dolor</p>
    <p class="p" style="margin-top:3px">Lorem ipsum dolor sit amet, consectetur adipiscing elit, sed do eiusmod tempor incididunt ut labore et dolore magna aliqua.</p>
    <p class="sub" style="font-size:7px;margin-top:10px">Lorem ipsum dolor</p>
    <p class="p" style="margin-top:3px">Lorem ipsum dolor sit amet, consectetur adipiscing elit, sed do eiusmod tempor incididunt ut labore et dolore magna aliqua.</p>
  </div>
  <div class="bar" style="left:366px;height:170px"><i style="height:55%;background:var(--purple)"></i><em style="background:var(--purple)">55%</em></div>
  <div class="bar" style="left:406px;height:170px"><i style="height:80%;background:var(--blue)"></i><em style="background:var(--blue)">80%</em></div>
  <div class="bar" style="left:446px;height:170px"><i style="height:60%;background:#2e5d9c"></i><em style="background:#2e5d9c">60%</em></div>
  <div class="bar" style="left:486px;height:170px"><i style="height:90%;background:var(--teal)"></i><em style="background:var(--teal)">90%</em></div>
  <div class="footer-name">Meadowlark Crossing</div><div class="footer-line"></div><div class="footer-mark"></div>
</section>

<section class="slide" style="left:615px;top:1905px;width:558px;height:314px">
  <div class="photo photo-seedlings" role="img" aria-label="Photo of a hand watering a row of seedlings"></div>
  <div class="abs" style="left:150px;top:12px;width:1px;height:280px;background:rgba(255,255,255,.8)"></div>
  <div class="abs" style="left:20px;top:14px;width:124px;display:flex;flex-direction:column;gap:22px">
    <div class="contact-line"><svg width="16" height="16" viewBox="0 0 16 16" fill="none" stroke="#fff" stroke-width="1.4"><circle cx="8" cy="8" r="7"/><ellipse cx="8" cy="8" rx="3" ry="7"/><path d="M1 8 H15"/></svg>www.meadowlarkcrossing.com</div>
    <div class="contact-line"><svg width="16" height="16" viewBox="0 0 16 16"><path d="M3 1 L6 1 L7 5 L5 6 Q6 9 10 11 L11 9 L15 10 L15 13 Q14 15 12 15 Q2 13 1 3 Q1 1 3 1 Z" fill="#fff"/></svg>+1 555 010 2040</div>
    <div class="contact-line"><svg width="18" height="14" viewBox="0 0 18 14"><rect width="18" height="14" fill="#fff"/><path d="M0 0 L9 8 L18 0" fill="none" stroke="#4a6a2a" stroke-width="1.2"/></svg>hello@meadowlarkcrossing.com</div>
    <div class="contact-line"><svg width="14" height="18" viewBox="0 0 14 18"><path d="M7 18 Q0 9 0 7 A7 7 0 0 1 14 7 Q14 9 7 18 Z" fill="#fff"/><circle cx="7" cy="7" r="2.5" fill="#4a6a2a"/></svg>48 Linden Row, Fairbrook,<br>USA</div>
  </div>
  <div class="contact-title" style="left:160px;top:138px;font-size:22px">CONTACT US</div>
</section>

<!-- Row 8 -->
<section class="slide" style="left:253px;top:2230px;width:689px;height:403px">
  <div class="photo photo-soil" role="img" aria-label="Photo of seedlings at different growth stages in soil"></div>
  <div class="contact-title" style="left:46px;top:158px;font-size:30px">CONTACT US</div>
  <div class="abs" style="left:36px;right:36px;top:308px;display:flex;justify-content:space-between;align-items:flex-start">
    <div class="contact-line" style="align-items:center"><svg width="28" height="28" viewBox="0 0 16 16" fill="none" stroke="#fff" stroke-width="1.2"><circle cx="8" cy="8" r="7"/><ellipse cx="8" cy="8" rx="3" ry="7"/><path d="M1 8 H15"/></svg>www.meadowlarkcrossing.com</div>
    <div class="contact-line" style="align-items:center"><svg width="26" height="26" viewBox="0 0 16 16"><path d="M3 1 L6 1 L7 5 L5 6 Q6 9 10 11 L11 9 L15 10 L15 13 Q14 15 12 15 Q2 13 1 3 Q1 1 3 1 Z" fill="#fff"/></svg>+1 555 010 2040</div>
    <div class="contact-line" style="align-items:center"><svg width="30" height="22" viewBox="0 0 18 14"><rect width="18" height="14" fill="#fff"/><path d="M0 0 L9 8 L18 0" fill="none" stroke="#4a3a2a" stroke-width="1.2"/></svg>hello@meadowlarkcrossing.com</div>
    <div class="contact-line" style="align-items:center;text-align:center"><svg width="22" height="28" viewBox="0 0 14 18"><path d="M7 18 Q0 9 0 7 A7 7 0 0 1 14 7 Q14 9 7 18 Z" fill="#fff"/><circle cx="7" cy="7" r="2.5" fill="#4a3a2a"/></svg>48 Linden Row, Fairbrook,<br>USA</div>
  </div>
</section>

</main>
</body>
</html>
```